Business Card & Stationary Design for a PI Law Firm
Trial Attorneys Representing Injured Persons
I need double sided standard sized Business Card [3.5" x 2"]
use clean, modern fonts (ex: similar to a century gothic)
Bright & Fun-filled
Gregory T. Vasko
Vasko Legal Partners, LLC
418 N. Harlowe
Suite 0714
Chicago, IL 60417
vaskolegal@mailvo.net
www.vaskolegalpartners.net
Trial Attorneys Representing Injured Persons (Insert this tag line)
BUSINESS CARDS – double sided
The options are to do an assortment (up to 3) of the following:
1. front side in chocolate brown and back side in white (OR)
2. front side in the slate grey and back side in white
3. front side in lime green and back side in white
4. front side in orange and back side in white
STATIONARY:
The options are to utilize an assortment (up to 3) of the following options:
1. white background
2. white background with contrasting design elements in lime green
3. white background with contrasting design elements in orange
4. white background with contrasting design elements in chocolate brown
5. white background with contrasting design elements in slate grey
6. OR any combination of the above colors
ENVELOPES:
The options are to utilize an assortment (up to 3) of the following color options:
1. chocolate brown background
2. slate grey background
3. white background with contrast envelope fold color in slate grey
4. White background with contrast envelope fold chocolate brown
5. white background with contrast envelope fold in the lime green
6.. white background with contrast envelope fold in the orange
7. OR any combination of the above colors
WATERMARK-LIKE GRAPHICS in Stationary, Envelopes and Cards:
We would like to see a creative use of graphics for watermarks or shadows in the background of the business cards, stationery and envelopes. They can be colorful in lime green or orange or a combo of both or in chocolate brown and / or slate grey, but not too dark in saturation (as to be able to see any fonts).
LAYOUT for Cards and Stationary:
1. The layout should be clean and modern and utilize attractive and modern graphic symbols or mod bullet type points before each line of contact information.
2. Open to vertical layout or horizontal on business card.
3. Please include web address on envelope design perhaps in a separate area of the envelope from the return address.
White version

```html
<!DOCTYPE html>
<html lang="en">
<head>
<meta charset="utf-8">
<title>Vasko Legal Partners — Stationery Set</title>
<link href="https://fonts.googleapis.com/css2?family=Didact+Gothic&display=swap" rel="stylesheet">
<style>
  :root{
    --orange:#f26a1b;
    --lime:#8cc63f;
    --brown:#4a2a1a;
    --slate:#5f6366;
    --paper:#ffffff;
    --stage:#ece8e2;
    --ink:#5a5a5a;
    --label:#7a6f64;
    --cream:#f3e6d8;
  }
  *{box-sizing:border-box;margin:0;padding:0}
  html,body{width:1200px;height:446px;overflow:hidden}
  body{background:var(--stage);font-family:"Didact Gothic",sans-serif;color:var(--ink);position:relative}
  .piece{position:absolute;background:var(--paper);box-shadow:0 2px 6px rgba(0,0,0,.18);overflow:hidden}
  .piece svg.art{position:absolute;inset:0;width:100%;height:100%}
  .label{position:absolute;font-size:7px;letter-spacing:.5px;text-transform:uppercase;color:var(--label);white-space:nowrap}

  .firm-name{position:absolute;color:var(--slate);font-weight:400;line-height:1.15;letter-spacing:.3px;white-space:nowrap}
  .firm-name.stacked{white-space:normal}
  .firm-name.on-dark{color:var(--cream)}

  .contact{position:absolute;list-style:none;font-size:4.5px;line-height:7px;color:var(--ink);white-space:nowrap}
  .contact li::before{content:"";display:inline-block;width:3px;height:3px;border-radius:50%;background:var(--lime);margin-right:3px;vertical-align:middle}
  .watermark{position:absolute;border-radius:50%;background:radial-gradient(ellipse at center,rgba(140,198,63,.18),rgba(242,106,27,.08) 60%,rgba(255,255,255,0) 75%)}
  .footer-line{position:absolute;left:0;right:0;text-align:center;font-size:4.5px;color:var(--ink);white-space:nowrap}
  .web{position:absolute;left:0;right:0;text-align:center;font-size:4.5px;color:var(--slate);white-space:nowrap}

  .card-front{left:36px;top:233px;width:120px;height:69px}
  .card-front .panel{position:absolute;left:0;top:0;bottom:0;width:48px;background:var(--orange);color:#fff;font-size:3.8px;line-height:6px;padding:14px 4px;white-space:nowrap}
  .card-back{left:36px;top:329px;width:120px;height:69px;background:var(--brown)}
  .card-back .tagline{position:absolute;left:0;right:0;top:46px;text-align:center;color:var(--cream);font-size:4.3px;white-space:nowrap}
</style>
</head>
<body>

<div class="label" style="left:36px;top:189px">Stationery Design</div>

<div class="piece card-front">
  <div class="panel">Gregory T. Vasko<br>418 N. Harlowe<br>Suite 0714<br>Chicago, IL 60417</div>
  <div class="firm-name stacked" style="left:56px;top:24px;width:60px;font-size:8px">Vasko<br>Legal Partners</div>
</div>
<div class="label" style="left:36px;top:307px">Business Card Front</div>

<div class="piece card-back">
  <div class="firm-name on-dark" style="left:0;right:0;top:24px;text-align:center;font-size:8px">Vasko Legal Partners</div>
  <div class="tagline">Trial Attorneys Representing Injured Persons</div>
</div>
<div class="label" style="left:36px;top:403px">Business Card Back</div>

<div class="piece" style="left:180px;top:12px;width:276px;height:372px">
  <svg class="art" viewBox="0 0 276 372" preserveAspectRatio="none">
    <path d="M0 0H24Q10 186 24 372H0Z" fill="var(--orange)"/>
    <path d="M30 0Q16 186 30 372" fill="none" stroke="var(--lime)" stroke-width="4"/>
  </svg>
  <div class="firm-name" style="left:46px;top:20px;font-size:12px">Vasko Legal Partners</div>
  <ul class="contact" style="left:196px;top:16px">
    <li>418 N. Harlowe, Suite 0714</li>
    <li>Chicago, IL 60417</li>
    <li>vaskolegal@mailvo.net</li>
    <li>www.vaskolegalpartners.net</li>
  </ul>
  <div class="watermark" role="img" aria-label="Faint vehicle watermark graphic" style="left:70px;top:270px;width:160px;height:96px"></div>
</div>
<div class="label" style="left:280px;top:403px">Letterhead Option 1</div>

<div class="piece" style="left:475px;top:12px;width:336px;height:372px">
  <svg class="art" viewBox="0 0 336 372" preserveAspectRatio="none">
    <path d="M0 0H20Q8 186 20 372H0Z" fill="var(--orange)"/>
    <path d="M336 0H318Q330 186 318 372H336Z" fill="var(--lime)"/>
    <path d="M312 0Q324 186 312 372" fill="none" stroke="var(--orange)" stroke-width="3"/>
  </svg>
  <div class="firm-name" style="left:0;right:0;top:20px;text-align:center;font-size:14px">Vasko Legal Partners</div>
  <div class="watermark" role="img" aria-label="Faint vehicle watermark graphic" style="left:108px;top:150px;width:130px;height:90px"></div>
  <div class="footer-line" style="top:352px">418 N. Harlowe, Suite 0714 · Chicago, IL 60417 · vaskolegal@mailvo.net · www.vaskolegalpartners.net</div>
</div>
<div class="label" style="left:600px;top:403px">Letterhead Option 2</div>

<div class="piece" style="left:828px;top:252px;width:180px;height:114px">
  <svg class="art" viewBox="0 0 180 114" preserveAspectRatio="none">
    <path d="M0 114V70Q60 96 180 100V114Z" fill="var(--orange)"/>
    <path d="M0 66Q60 92 180 96" fill="none" stroke="var(--lime)" stroke-width="3"/>
  </svg>
  <div class="firm-name" style="left:10px;top:11px;font-size:8px">Vasko Legal Partners</div>
  <div class="watermark" role="img" aria-label="Faint vehicle watermark graphic" style="left:110px;top:30px;width:60px;height:40px"></div>
</div>
<div class="label" style="left:870px;top:372px">Envelope Option 1</div>

<div class="piece" style="left:924px;top:12px;width:264px;height:92px">
  <svg class="art" viewBox="0 0 264 92" preserveAspectRatio="none">
    <rect width="264" height="44" fill="var(--orange)"/>
  </svg>
</div>
<div class="piece" style="left:924px;top:112px;width:264px;height:96px">
  <svg class="art" viewBox="0 0 264 96" preserveAspectRatio="none">
    <path d="M0 0H264V28L140 54H124L0 28Z" fill="var(--lime)"/>
  </svg>
</div>
<div class="piece" style="left:924px;top:216px;width:264px;height:126px">
  <svg class="art" viewBox="0 0 264 126" preserveAspectRatio="none">
    <path d="M0 0L132 62L264 0" fill="none" stroke="#e6e6e6" stroke-width="1"/>
  </svg>
  <div class="firm-name" style="left:0;right:0;top:50px;text-align:center;font-size:8px">Vasko Legal Partners</div>
  <div class="web" style="top:64px">www.vaskolegalpartners.net</div>
</div>
<div class="label" style="left:1060px;top:403px">Envelope Option 2</div>

</body>
</html>
```